OPF - Brochure 52 week Curriculum

Oak Path Fellows, Inc. wants to create a distribution Brochure. In the Bible (Matthew 28:18-20)- JESUS said to "TEACH" others what HE has commanded. we want to "PUT IN PRINT"

these 52 lines summarize HIS teachings
we want to use as our Curriculum teaching men ...

incorporate our statements and two main passages of scripture
(see attach pictures of headquarter lobby) to brand uniformity and consistency... we have summarized into 52 groups, but its NOT required to have numbers...
Purpose = obey GOD
Mission = love others
Vision = Development God fearing men globally.

The designer can have freedom in layout and sizing.
we were thinking bi fold , but again... designer has freedom
Please incorporate our colors (white, black, gray) using color wheel provided and our LOGO with website.

```html
<!DOCTYPE html>
<html lang="en">
<head>
<meta charset="utf-8">
<title>Oak Path Fellows – Teachings of Jesus Brochure</title>
<link href="https://fonts.googleapis.com/css2?family=Montserrat:wght@400;500;700;800&display=swap" rel="stylesheet">
<style>
  :root{
    --backdrop:#ddd3b6;
    --paper:#f1f1f1;
    --ink:#111111;
    --ink-soft:#2a2a2a;
    --white:#ffffff;
    --gray:#8a8a8a;
    --glow-top:#d9b469;
    --glow-mid:#8c7a4c;
    --shadow-dark:#141414;
  }
  *{box-sizing:border-box;margin:0;padding:0}
  html,body{width:1200px;height:840px;overflow:hidden}
  body{
    background:var(--backdrop);
    font-family:'Montserrat',sans-serif;
    display:flex;align-items:center;justify-content:center;
  }
  .spread{display:flex;width:1160px;height:750px;box-shadow:0 10px 30px rgba(0,0,0,.18)}
  .page{width:580px;height:750px;position:relative;overflow:hidden}

  /* Back cover */
  .back-cover{background:var(--paper);color:var(--ink);padding:70px 58px 0}
  .brand{text-align:center}
  .brand-name{font-weight:800;font-size:86px;line-height:1;letter-spacing:2px}
  .brand-url{font-weight:700;font-size:13px;letter-spacing:.5px;margin-top:6px}
  .pillars{display:flex;align-items:flex-start;justify-content:center;gap:22px;margin-top:48px}
  .pillar-title{font-weight:800;font-size:30px;line-height:1}
  .pillar-sub{font-weight:700;font-size:12px;margin-top:3px}
  .pillar-divider{width:2px;height:48px;background:var(--ink);transform:skewX(-12deg)}
  .scripture{font-size:11.5px;line-height:1.5;text-align:justify;color:var(--ink-soft);margin-top:18px}
  .citation{font-style:italic;font-size:10.5px;text-align:right;margin-top:8px;color:var(--ink-soft)}
  .vision{margin-top:34px}
  .vision-title{font-weight:800;font-size:32px;line-height:1}
  .vision-sub{font-weight:700;font-size:13px;margin-top:4px}

  /* Front cover */
  .front-cover{color:var(--white)}
  .cover-art{position:absolute;inset:0;
    background:
      radial-gradient(ellipse at 60% 28%, rgba(245,215,140,.95) 0%, rgba(200,160,90,.6) 30%, rgba(0,0,0,0) 60%),
      linear-gradient(180deg,var(--glow-top) 0%,var(--glow-mid) 38%,#3a3226 62%,var(--shadow-dark) 82%)}
  .cover-content{position:absolute;left:0;right:0;top:430px;text-align:center}
  .cover-title{font-weight:800;line-height:.95;text-transform:uppercase}
  .cover-title .line-1{display:block;font-size:54px;letter-spacing:1px}
  .cover-title .line-2{display:block;font-size:64px}
  .cover-title .small{font-size:36px}
  .cover-rule{width:340px;height:2px;background:var(--white);margin:18px auto 14px}
  .cover-ref{font-weight:700;font-size:24px;letter-spacing:.5px}
  .cover-brand{margin-top:30px}
  .cover-brand .brand-name{font-size:72px}
  .cover-brand .brand-url{font-size:12px}
</style>
</head>
<body>
  <main class="spread">
    <section class="page back-cover">
      <header class="brand">
        <div class="brand-name">OPF</div>
        <div class="brand-url">WWW.OAKPATHFELLOWS.COM</div>
      </header>

      <div class="pillars">
        <div class="pillar">
          <div class="pillar-title">Obey God</div>
          <div class="pillar-sub">Our Purpose</div>
        </div>
        <div class="pillar-divider"></div>
        <div class="pillar">
          <div class="pillar-title">Love Others</div>
          <div class="pillar-sub">Our Mission</div>
        </div>
      </div>
      <p class="scripture">Jesus replied: “‘Love the Lord your God with all your heart and with all your soul and with all your mind.’ This is the first and greatest commandment. And the second is like it: ‘Love your neighbor as yourself.’ All the Law and the Prophets hang on these two commandments.”</p>
      <p class="citation">Matthew 22:37-40</p>

      <div class="vision">
        <div class="vision-title">Our Vision</div>
        <div class="vision-sub">Develop God Fearing Men Globally</div>
        <p class="scripture">Then Jesus came to them and said, “All authority in heaven and on earth has been given to me. Therefore go and make disciples of all nations, baptizing them in the name of the Father and of the Son and of the Holy Spirit, and teaching them to obey everything I have commanded you. And surely I am with you always, to the very end of the age.”</p>
        <p class="citation">Matthew 28:18-20</p>
      </div>
    </section>

    <section class="page front-cover">
      <div class="cover-art" role="img" aria-label="Painted scene of Jesus teaching a gathered crowd in a sunlit forest"></div>
      <div class="cover-content">
        <h1 class="cover-title">
          <span class="line-1">Teachings</span>
          <span class="line-2"><span class="small">of</span> Jesus</span>
        </h1>
        <div class="cover-rule"></div>
        <div class="cover-ref">Matthew 28:18-20</div>
        <div class="brand cover-brand">
          <div class="brand-name">OPF</div>
          <div class="brand-url">WWW.OAKPATHFELLOWS.COM</div>
        </div>
      </div>
    </section>
  </main>
</body>
</html>
```